Pumper Septic Truck Design

Need a truck design that compliments our exisiting truck's graphics and design. Colors should remain blue and silver. I have provided an example of our current truck and of the new truck that we would like to have designed. We really like pinstripe type designs on the cab and a waviness to the design.

Requirements
Must have
• 1-Colors to remain blue and silver
2-Cab should only have graphics, no text.
3-Company name in the design is Brookvale Septic to match existing text on old truck.

```html
<!DOCTYPE html>
<html lang="en">
<head>
<meta charset="utf-8">
<title>Brookvale Septic – Tank Graphic</title>
<link href="https://fonts.googleapis.com/css2?family=Roboto+Condensed:wght@700&family=Roboto+Slab:wght@400;700&display=swap" rel="stylesheet">
<style>
  :root {
    --page-bg: #e4e5e7;
    --panel-white: #f7f7f7;
    --panel-stripe: #ececec;
    --band-grey: #666668;
    --band-grey-light: #747476;
    --brand-navy: #2e3192;
    --brand-blue: #1273bb;
    --text-white: #ffffff;
  }
  * { margin: 0; padding: 0; box-sizing: border-box; }
  html, body {
    width: 1152px;
    height: 1200px;
    overflow: hidden;
    background: var(--page-bg);
  }
  .canvas {
    position: relative;
    width: 1152px;
    height: 1200px;
  }
  .tank-graphic {
    position: absolute;
    left: 36px;
    top: 438px;
    width: 1080px;
    height: 324px;
    overflow: hidden;
    box-shadow: 0 18px 30px rgba(0, 0, 0, 0.18);
  }
  .stripe-field {
    position: absolute;
    left: 0;
    top: 0;
    width: 100%;
    height: 233px;
    background: linear-gradient(180deg, var(--panel-white), var(--panel-stripe));
  }
  .grey-band {
    position: absolute;
    left: 0;
    top: 233px;
    width: 100%;
    height: 91px;
    background: linear-gradient(180deg, var(--band-grey-light), var(--band-grey));
  }
  .company-name {
    position: absolute;
    left: 0;
    top: 128px;
    width: 100%;
    text-align: center;
    font-family: "Roboto Condensed", sans-serif;
    font-weight: 700;
    font-size: 58px;
    line-height: 70px;
    letter-spacing: 1px;
    color: var(--brand-navy);
  }
  .phone-bar {
    position: absolute;
    left: 319px;
    top: 209px;
    width: 442px;
    height: 47px;
  }
  .phone-bar svg { position: absolute; left: 0; top: 0; }
  .phone-number {
    position: absolute;
    left: 82px;
    top: 0;
    width: 330px;
    height: 47px;
    text-align: center;
    font-family: "Roboto Condensed", sans-serif;
    font-weight: 700;
    font-size: 42px;
    line-height: 47px;
    color: var(--text-white);
  }
  .web-address {
    position: absolute;
    left: 0;
    top: 268px;
    width: 100%;
    text-align: center;
    font-family: "Roboto Slab", serif;
    font-size: 22px;
    line-height: 30px;
    letter-spacing: 6px;
    color: var(--text-white);
  }
  .web-address strong { font-weight: 700; }
</style>
</head>
<body>
<main class="canvas">
  <section class="tank-graphic">
    <div class="stripe-field" role="img" aria-label="Light grey diagonal stripe pattern on white"></div>
    <div class="grey-band" role="img" aria-label="Dark grey diagonal stripe band"></div>

    <h1 class="company-name">Brookvale Septic</h1>

    <div class="phone-bar">
      <svg width="442" height="47" viewBox="0 0 442 47" aria-hidden="true">
        <polygon class="phone-bar-tab" points="14,0 76,0 59,47 0,47" fill="#1273bb"/>
        <polygon class="phone-bar-main" points="76,0 442,0 427,47 59,47" fill="#2e3192"/>
        <g class="phone-icon" transform="translate(38,23.5)" fill="none" stroke="#ffffff" stroke-width="2">
          <circle r="14"/>
          <path d="M-5,-8 l3,-1 l2,5 l-2,2 q1,4 5,6 l2,-2 l5,2 l-1,3 q-3,3 -8,0 q-6,-4 -8,-9 q-1,-4 2,-6 z" fill="#ffffff" stroke="none"/>
        </g>
      </svg>
      <div class="phone-number">555-208-4416</div>
    </div>

    <p class="web-address">www.<strong>brookvaleseptic</strong>.com</p>
  </section>
</main>
</body>
</html>
```